Business card

I need a business card design for my consulting company in animal welfare for livestock. I like clean, crisp, simple.

One I imagined was double-sided:
side1: just my name and contact information
side2: silhouette of farm animals. Could be 3 (pig, cow, chicken) or all the species (pig, cow, chicken, duck, sheep, rabbit, etc) that continue the length of the card. I have attached an image of a silhouette style.

But, I am open to any concept.

Industry/Entity Type

Business

```html
<!DOCTYPE html>
<html lang="en">
<head>
<meta charset="utf-8">
<title>Helen Marwick – Business Card</title>
<link rel="stylesheet" href="https://fonts.googleapis.com/css2?family=Pacifico&family=Poiret+One&family=Open+Sans:wght@400&display=swap">
<style>
  :root {
    --backdrop: #c9c9c9;
    --card-white: #ffffff;
    --brand-green: #62bb46;
    --silhouette-dark: #333333;
    --watermark-grey: #e4e4e4;
    --text-dark: #2a2a2a;
    --tagline-grey: #3c3c3c;
  }
  * { margin: 0; padding: 0; box-sizing: border-box; }
  html, body {
    width: 1200px;
    height: 900px;
    overflow: hidden;
    background: var(--backdrop);
  }
  .canvas {
    position: relative;
    width: 1200px;
    height: 900px;
  }
  .card {
    position: absolute;
    top: 300px;
    width: 520px;
    height: 298px;
    border-radius: 22px;
    overflow: hidden;
  }
  /* Front side */
  .card--front {
    left: 55px;
    background: var(--card-white);
  }
  .card__frame {
    position: absolute;
    inset: 12px;
    border: 8px solid var(--brand-green);
    border-radius: 18px;
  }
  .card__watermark {
    position: absolute;
    left: 28px;
    top: 92px;
    width: 470px;
    height: 86px;
    border-radius: 14px;
    background: linear-gradient(90deg, var(--watermark-grey), #efefef 50%, var(--watermark-grey));
    opacity: 0.8;
  }
  .card__identity {
    position: absolute;
    left: 0;
    right: 0;
    top: 100px;
    text-align: center;
  }
  .card__name {
    font-family: "Pacifico", cursive;
    font-size: 42px;
    line-height: 1.1;
    color: var(--brand-green);
    letter-spacing: 1px;
  }
  .card__tagline {
    font-family: "Poiret One", sans-serif;
    font-size: 17px;
    font-weight: 400;
    color: var(--tagline-grey);
    margin-top: 2px;
  }
  .card__contact {
    position: absolute;
    left: 0;
    right: 0;
    top: 210px;
    text-align: center;
    font-family: "Open Sans", sans-serif;
    color: var(--text-dark);
    font-style: normal;
  }
  .card__phone { font-size: 17px; letter-spacing: 0.5px; }
  .card__email { font-size: 14px; margin-top: 6px; letter-spacing: 0.4px; }

  /* Back side */
  .card--back {
    left: 625px;
    background: var(--brand-green);
  }
  .card__animal-parade {
    position: absolute;
    left: 30px;
    top: 112px;
    width: 460px;
    height: 74px;
    border-radius: 10px;
    background: var(--silhouette-dark);
  }
</style>
</head>
<body>
  <main class="canvas">
    <section class="card card--front" aria-label="Business card front">
      <div class="card__frame"></div>
      <div class="card__watermark" role="img" aria-label="Faint grey silhouettes of a sheep, cow and rooster behind the name"></div>
      <div class="card__identity">
        <h1 class="card__name">Helen Marwick</h1>
        <p class="card__tagline">Welfare Services for Livestock Stakeholders</p>
      </div>
      <address class="card__contact">
        <p class="card__phone">+1.555.014.2290</p>
        <p class="card__email">helen.marwick@example.com</p>
      </address>
    </section>

    <section class="card card--back" aria-label="Business card back">
      <div class="card__animal-parade" role="img" aria-label="Row of dark silhouettes: sheep, rabbit, pig, duck, cow and rooster"></div>
    </section>
  </main>
</body>
</html>
```